Australian Web Design company needs a business card design

We need a business card design for a Sydney based Web Design/Development company called "Blue Pine Web Design". We design, build and deploy websites for small to medium sized businesses. The final design should be clean and communicate that we are a professional and supportive company.
I'd like the Icon to be abstract. Something that embodies the power of the internet, needs to be clean/professional and show that we are human and that we support our customers. Hope that helps.
Target Market(s)
All small to medium businesses
Industry/Entity Type
Business
Contact Information for Business Card
Gordon Whitcombe
Blue Pine Web Design
17 Calloway Brook Road
East Gosford
NSW 2250
0438 572 614
gordon@bluepinewebdesign.com.au
www.bluepinewebdesign.com.au

```html
<!DOCTYPE html>
<html lang="en">
<head>
<meta charset="utf-8">
<title>Blue Pine Web Design – Business Card</title>
<link href="https://fonts.googleapis.com/css2?family=Arimo:wght@400;700&display=swap" rel="stylesheet">
<style>
  :root {
    --stage: #161616;
    --brand-red: #f0243a;
    --brand-red-deep: #d81e31;
    --accent-blue: #2ba6c6;
    --card-white: #ffffff;
    --card-shade: #ececec;
    --ink: #111111;
    --ink-soft: #333333;
  }
  * { box-sizing: border-box; margin: 0; padding: 0; }
  html, body {
    width: 1200px; height: 1000px; overflow: hidden;
    background: var(--stage);
    font-family: "Arimo", Arial, sans-serif;
  }
  .stage {
    position: relative; width: 1200px; height: 1000px;
    display: flex; flex-direction: column; align-items: center; justify-content: center; gap: 60px;
  }
  .card {
    position: relative; width: 700px; height: 400px; overflow: hidden;
  }

  /* Front: red face with brand name */
  .card--front {
    background: radial-gradient(ellipse at 55% 35%, #ff2a40 0%, var(--brand-red) 45%, var(--brand-red-deep) 100%);
  }
  .card--front .brand {
    position: absolute; left: 150px; top: 130px;
    display: flex; align-items: center; gap: 22px;
    color: var(--card-white);
  }
  .brand__mark {
    width: 110px; height: 110px; background: var(--card-white); flex: none;
  }
  .brand__name {
    font-weight: 700; line-height: 1; text-transform: uppercase;
  }
  .brand__name-main { display: block; font-size: 60px; letter-spacing: 1px; }
  .brand__name-sub { display: block; font-size: 26px; margin-top: 6px; }

  /* Back: white face with contact details */
  .card--back {
    background: linear-gradient(180deg, var(--card-white) 0%, #f7f7f7 60%, var(--card-shade) 100%);
    color: var(--ink);
  }
  .accent-bar {
    position: absolute; left: 0; top: 130px; width: 11px; height: 210px;
    background: var(--accent-blue);
  }
  .card--back .brand {
    position: absolute; right: 70px; top: 60px;
    display: flex; align-items: center; gap: 16px;
    color: var(--brand-red);
  }
  .card--back .brand__mark { width: 84px; height: 84px; background: var(--brand-red); }
  .card--back .brand__name-main { font-size: 44px; }
  .card--back .brand__name-sub { font-size: 20px; margin-top: 4px; }

  .holder { position: absolute; left: 75px; top: 150px; }
  .holder__name { font-size: 24px; font-weight: 700; }
  .holder__role { font-size: 17px; margin-top: 8px; color: var(--ink-soft); }

  .divider {
    position: absolute; left: 240px; right: 0; top: 205px; height: 3px;
    background: var(--brand-red);
  }

  .contact {
    position: absolute; left: 60px; top: 245px;
    list-style: none; font-size: 18px; color: var(--ink-soft); line-height: 32px;
  }
  .contact__label { margin-right: 6px; }
</style>
</head>
<body>
  <main class="stage">
    <section class="card card--front" aria-label="Card front">
      <div class="brand">
        <span class="brand__mark" aria-hidden="true"></span>
        <span class="brand__name">
          <span class="brand__name-main">Blue Pine</span>
          <span class="brand__name-sub">Web Design</span>
        </span>
      </div>
    </section>

    <section class="card card--back" aria-label="Card back">
      <span class="accent-bar" aria-hidden="true"></span>
      <div class="brand">
        <span class="brand__mark" aria-hidden="true"></span>
        <span class="brand__name">
          <span class="brand__name-main">Blue Pine</span>
          <span class="brand__name-sub">Web Design</span>
        </span>
      </div>
      <div class="holder">
        <p class="holder__name">Gordon Whitcombe</p>
        <p class="holder__role">CEO &amp; Founder</p>
      </div>
      <span class="divider" aria-hidden="true"></span>
      <ul class="contact">
        <li><span class="contact__label">p :</span>0438 572 614</li>
        <li><span class="contact__label">e :</span>gordon@bluepinewebdesign.com.au</li>
        <li><span class="contact__label">w :</span>www.bluepinewebdesign.com.au</li>
        <li><span class="contact__label">fb :</span>facebook.com/bluepinedesign</li>
      </ul>
    </section>
  </main>
</body>
</html>
```